Need 2 sided card for Loomfield Goods Co. Logo supplied.

I am looking for a business card for my online craft supply business.

I have a very simple design already which I am kind of happy with (see attached pdf) - but would like suggestions for something a little more creative. Design MUST be clean. Super clean! Think thin lines and not blocks of color...

Design must be clean and crisp. No other colors other than in palette (see link below)

I would also like to possible incorporate my tagline - maybe on the front but definitely on the back:
"HollowReed Ideas & Hobby Materials"

Logo file is supplied, but I think spacing on the card may required the wording to be moved underneaths the camera icon - which is fine. Font in logo is Maven Pro. OPEN TO USE OF OTHER FONTS ON CARD BUT MUST BE CLEAN DESIGN.

FRONT OF CARD
All information on attached pdf is correct and should be shown in your design.

BACK OF CARD
Needs to show www.tindalerow.example and maybe logo repeat and tagline.

SIZE
New Zealand sized - meaning finished card will be 90 x 55mm
Printing requirements: printed area is 90mm x 55mm with a 2mm bleed all round.

COLORS
Color palette used in logo can be seen here for HEX and RGB reference: http://www.huebankly.example/palette/8627410/website

NOTE: PAYMENT WILL BE MADE FOR THE BEST DESIGN - EVEN IF I DECIDE NOT TO USE IT.
Updates

Thank you all so much for your designs. I will be providing feedback to ALL designers tomorrow. This weekend is a holiday weekend here in New Zealand and so no work for a few days. Thank-you again - I appreciate your time and creativity!

Industry/Entity Type

Camera

Font styles to use
Other font styles liked:
• Maven Pro - open to others

Requirements
Must have
• Clean design. Logo must be prominent for brand recognition. All contact information must be shown.
Nice to have
• Tagline - at least on reverse

```html
<!DOCTYPE html>
<html lang="en">
<head>
<meta charset="utf-8">
<title>Loomfield Goods Co. — Business Card</title>
<link href="https://fonts.googleapis.com/css2?family=Maven+Pro:wght@400;500&family=Roboto+Condensed:wght@400;700&display=swap" rel="stylesheet">
<style>
  :root{
    --stage:#e9e6e0;
    --paper:#ffffff;
    --slate:#5c5c5e;
    --slate-dark:#4a4a4c;
    --citron:#c8bf2e;
    --ink:#4d4d4f;
    --accent:#e8563f;
  }
  *{margin:0;padding:0;box-sizing:border-box}
  html,body{width:1200px;height:682px;overflow:hidden;background:var(--stage)}
  .stage{position:relative;width:1200px;height:682px}
  .card{position:absolute;top:176px;width:540px;height:330px;box-shadow:0 6px 18px rgba(0,0,0,.18)}
  .card--front{left:40px;background:var(--paper);overflow:hidden}
  .card--back{left:620px;background:var(--slate);overflow:hidden}

  .title-band{position:absolute;left:212px;top:0;right:0;height:30px;background:var(--slate);
    display:flex;align-items:center;justify-content:flex-end;padding-right:22px}
  .job-title{font-family:"Roboto Condensed",sans-serif;color:var(--paper);font-size:12px;letter-spacing:2px}

  .brand{position:absolute;left:28px;top:104px;width:160px;text-align:center}
  .brand-dot{width:44px;height:44px;border-radius:50%;background:var(--accent);margin:0 auto 12px}
  .brand-name{font-family:"Maven Pro",sans-serif;font-weight:500;font-size:22px;line-height:1.15;color:var(--slate)}

  .name-row{position:absolute;left:212px;top:62px;display:flex;height:36px}
  .name-badge{width:36px;height:36px;background:var(--citron)}
  .name-bar{background:var(--slate);padding:0 20px 0 14px;display:flex;align-items:center}
  .person-name{font-family:"Roboto Condensed",sans-serif;font-weight:700;font-size:20px;letter-spacing:1.5px;color:var(--paper)}

  .contacts{position:absolute;left:222px;top:124px;display:grid;grid-template-columns:130px 190px;row-gap:16px}
  .contact{display:flex;align-items:center;gap:8px;font-family:"Roboto Condensed",sans-serif;font-size:12px;color:var(--ink)}
  .contact svg{width:13px;height:13px;flex:none}

  .address-band{position:absolute;left:176px;right:0;top:224px;height:32px;background:var(--citron);
    display:flex;align-items:center;gap:8px;padding-left:48px}
  .address-band svg{width:12px;height:14px}
  .address{font-family:"Roboto Condensed",sans-serif;font-size:12px;color:var(--paper);letter-spacing:.5px}
  .corner-block{position:absolute;left:28px;top:224px;width:132px;height:32px;border-bottom:3px solid var(--citron)}

  .back-brand{position:absolute;left:0;right:0;top:56px;text-align:center}
  .back-brand .brand-dot{width:48px;height:48px;margin-bottom:14px}
  .back-brand .brand-name{color:var(--paper);font-size:26px}
  .tagline{margin-top:10px;font-family:"Roboto Condensed",sans-serif;font-size:13px;letter-spacing:1.5px;color:var(--paper)}
  .tagline-rule{width:60px;height:2px;background:var(--citron);margin:12px auto 0}
  .back-band{position:absolute;left:0;right:0;top:224px;height:32px;background:var(--slate-dark);
    display:flex;align-items:center;justify-content:center;gap:8px}
  .back-band svg{width:13px;height:13px}
  .back-web{font-family:"Roboto Condensed",sans-serif;font-size:13px;letter-spacing:1px;color:var(--paper)}
  .back-foot{position:absolute;left:0;right:0;top:256px;height:3px;background:var(--citron)}
</style>
</head>
<body>
<main class="stage">
  <section class="card card--front" aria-label="Card front">
    <div class="title-band"><span class="job-title">GENERAL MANAGER</span></div>

    <div class="brand">
      <div class="brand-dot"></div>
      <div class="brand-name">Loomfield<br>Goods Co.</div>
    </div>

    <div class="name-row">
      <div class="name-badge"></div>
      <div class="name-bar"><span class="person-name">ARLO BENNET</span></div>
    </div>

    <div class="contacts">
      <div class="contact">
        <svg viewBox="0 0 16 16"><path fill="#4d4d4f" d="M4 1l3 3-1.6 1.8a9 9 0 0 0 4.8 4.8L12 9l3 3-2 2.5C7 14 2 9 1.5 3z"/></svg>
        021 480 3172
      </div>
      <div class="contact">
        <svg viewBox="0 0 16 16"><rect x="1" y="3" width="14" height="10" fill="none" stroke="#4d4d4f" stroke-width="1.6"/><path d="M1 3l7 6 7-6" fill="none" stroke="#4d4d4f" stroke-width="1.6"/></svg>
        hello@tindalerow.example
      </div>
      <div class="contact">
        <svg viewBox="0 0 16 16"><rect x="4" y="1" width="8" height="14" rx="1.5" fill="none" stroke="#4d4d4f" stroke-width="1.6"/><circle cx="8" cy="12.5" r="1" fill="#4d4d4f"/></svg>
        021 480 3172
      </div>
      <div class="contact">
        <svg viewBox="0 0 16 16"><circle cx="8" cy="8" r="6.5" fill="none" stroke="#4d4d4f" stroke-width="1.4"/><ellipse cx="8" cy="8" rx="2.8" ry="6.5" fill="none" stroke="#4d4d4f" stroke-width="1.2"/><path d="M1.5 8h13" stroke="#4d4d4f" stroke-width="1.2"/></svg>
        www.tindalerow.example
      </div>
    </div>

    <div class="corner-block"></div>
    <div class="address-band">
      <svg viewBox="0 0 12 14"><path fill="#fff" d="M6 0a5 5 0 0 1 5 5c0 3.5-5 9-5 9S1 8.5 1 5a5 5 0 0 1 5-5z"/><circle cx="6" cy="5" r="1.8" fill="#c8bf2e"/></svg>
      <span class="address">Unit 14, Reed Lane, Loomfield 4021</span>
    </div>
  </section>

  <section class="card card--back" aria-label="Card back">
    <div class="back-brand">
      <div class="brand-dot"></div>
      <div class="brand-name">Loomfield Goods Co.</div>
      <p class="tagline">HollowReed Ideas &amp; Hobby Materials</p>
      <div class="tagline-rule"></div>
    </div>
    <div class="back-band">
      <svg viewBox="0 0 16 16"><circle cx="8" cy="8" r="6.5" fill="none" stroke="#ffffff" stroke-width="1.4"/><ellipse cx="8" cy="8" rx="2.8" ry="6.5" fill="none" stroke="#ffffff" stroke-width="1.2"/><path d="M1.5 8h13" stroke="#ffffff" stroke-width="1.2"/></svg>
      <span class="back-web">www.tindalerow.example</span>
    </div>
    <div class="back-foot"></div>
  </section>
</main>
</body>
</html>
```